Business Card Design. For a portrait and wedding photography business

Velvet Frame Studios Weddings, Portraits, Bar/Bat Mitzvah, Sweet 16's, On the Cutting Edge of Digital Photography Corporate Events High Quality Photography at an Affordable PricesCustom Wedding Packages.Custom Designed Album, Thank you cardsExpert Photo Editing and Retouching

Target Market(s)

Families for family portraits, head shots for business cards,, wedding clients, Suite 16's, bar/bat mitzvah, parties, and corporate events,
.

Industry/Entity Type

Wedding

Contact Information for Business Card

Daniel T. Ashworth 42 Linden Lane Harlow Glen, V.T. 12634 By Appointment Only

Font styles to use
Script
Other font styles liked:
• Time New Romen

Requirements
Must have
• I would like to use one of the photograph I uploaded I would prefer to let the designer choose based on their expertise.
Nice to have
• Leave it up to the designer
Should not have
• The card should not be too dark

```html
<!DOCTYPE html>
<html lang="en">
<head>
<meta charset="utf-8">
<title>Velvet Frame Studios – Business Card</title>
<link href="https://fonts.googleapis.com/css2?family=Alegreya:wght@400;500&family=Lato:wght@400&display=swap" rel="stylesheet">
<style>
  :root {
    --backdrop: #1f1f1f;
    --panel-light: #ececec;
    --panel-mid: #dcdcdc;
    --ink: #1c1c1c;
    --band: #2b2b2b;
    --band-text: #f2f2f2;
    --tab: #2f2f2f;
    --photo-dark: #3a3a3a;
    --photo-mid: #8a8a8a;
    --photo-light: #d6d6d6;
    --sheen: #f4f4f4;
  }
  * { margin: 0; padding: 0; box-sizing: border-box; }
  html, body {
    width: 1200px;
    height: 900px;
    overflow: hidden;
    background: var(--backdrop);
  }
  .canvas {
    position: relative;
    width: 1200px;
    height: 900px;
  }
  .business-card {
    position: absolute;
    left: 100px;
    top: 164px;
    width: 1000px;
    height: 572px;
    border-radius: 14px;
    overflow: hidden;
    background: linear-gradient(160deg, var(--panel-light) 0%, var(--panel-mid) 100%);
  }
  .card-photo {
    position: absolute;
    inset: 0;
    width: 1000px;
    height: 572px;
  }
  .name-tab {
    position: absolute;
    left: 0;
    top: 112px;
    width: 26px;
    height: 58px;
    background: var(--tab);
  }
  .holder-name {
    position: absolute;
    left: 54px;
    top: 108px;
    font-family: "Alegreya", "Times New Roman", serif;
    font-weight: 500;
    font-size: 44px;
    line-height: 1.2;
    color: var(--ink);
    letter-spacing: 0.5px;
    white-space: nowrap;
  }
  .holder-address {
    position: absolute;
    left: 54px;
    top: 218px;
    font-family: "Alegreya", "Times New Roman", serif;
    font-size: 26px;
    line-height: 40px;
    color: var(--ink);
    white-space: nowrap;
  }
  .appointment-band {
    position: absolute;
    left: 0;
    bottom: 0;
    width: 100%;
    height: 70px;
    background: var(--band);
    display: flex;
    align-items: center;
    justify-content: center;
    font-family: "Lato", "Helvetica", sans-serif;
    font-size: 20px;
    letter-spacing: 9px;
    color: var(--band-text);
    text-transform: uppercase;
  }
</style>
</head>
<body>
<main class="canvas">
  <section class="business-card">
    <svg class="card-photo" viewBox="0 0 1000 572" role="img" aria-label="Black and white wedding photograph: bride and groom kissing beside a garden fountain">
      <defs>
        <linearGradient id="photoTone" x1="0" y1="0" x2="1" y2="1">
          <stop offset="0" stop-color="#d6d6d6"/>
          <stop offset="0.45" stop-color="#8a8a8a"/>
          <stop offset="1" stop-color="#3a3a3a"/>
        </linearGradient>
      </defs>
      <polygon points="548,0 1000,0 1000,502 430,502" fill="#f4f4f4" opacity="0.8"/>
      <polygon points="562,0 1000,0 1000,502 446,502" fill="url(#photoTone)"/>
    </svg>
    <div class="name-tab"></div>
    <h1 class="holder-name">Daniel T. Ashworth</h1>
    <p class="holder-address">42 Linden Lane Harlow Glen,<br>V.T. 12634</p>
    <footer class="appointment-band">By Appointment Only</footer>
  </section>
</main>
</body>
</html>
```